Investor Presentation

We have a deck that is mostly finished that needs to be properly formatted and cleaned up. The presentation is for an investment in a financial firm. So the design we are looking for is very professional and minimalistic. A very clean look with conservative color schemes and fonts. The designer can leverage our existing logos, background, etc.

The final design files should have full editing functionality.

Target Market(s)

Sophisticated institutional investors

Industry/Entity Type

Conservative

Requirements
Nice to have
• Cleaned up / formatted tables from the attached files to add to the presentation.

```html
<!DOCTYPE html>
<html lang="en">
<head>
<meta charset="utf-8">
<title>Corvane Management – Investor Presentation Slides</title>
<link href="https://fonts.googleapis.com/css2?family=PT+Sans:ital,wght@0,400;0,700;1,400&family=PT+Sans+Narrow:wght@400;700&display=swap" rel="stylesheet">
<style>
  :root{
    --stage:#27302f;
    --teal:#148c91;
    --teal-dark:#0b6c70;
    --teal-light:#27a9ac;
    --ink:#2a2a2a;
    --body:#333;
    --navy:#2c3a7c;
    --paper:#f7f8f8;
    --paper-edge:#dfe2e3;
  }
  *{box-sizing:border-box;margin:0;padding:0}
  html,body{width:1200px;height:1000px;overflow:hidden;background:var(--stage)}
  body{position:relative;font-family:"PT Sans",sans-serif}

  .slide{position:absolute;width:568px;height:425px;overflow:hidden;
    background:radial-gradient(ellipse at 50% 45%,#ffffff 0%,var(--paper) 55%,var(--paper-edge) 100%);
    box-shadow:0 6px 18px rgba(0,0,0,.55)}
  .slide--tl{left:22px;top:50px}
  .slide--tr{left:610px;top:50px}
  .slide--bl{left:22px;top:525px}
  .slide--br{left:610px;top:525px}

  .backdrop-art{position:absolute;left:60px;top:20px;width:450px;height:330px;
    background:radial-gradient(ellipse at 50% 60%,rgba(160,205,210,.28),rgba(160,205,210,0) 70%)}

  .header-band{position:absolute;left:0;top:0;width:100%;height:43px;
    background:linear-gradient(#1fa0a4,var(--teal-dark));border-bottom:2px solid #0a5a5d;
    color:#fff;font-family:"PT Sans Narrow",sans-serif;font-weight:700;
    display:flex;align-items:center;justify-content:center}
  .header-band--small{font-size:21px}
  .header-band--large{font-size:24px}

  .footer-band{position:absolute;left:0;bottom:0;width:100%;height:42px;
    background:linear-gradient(#1a9ca0,var(--teal-dark));border-top:2px solid #0d7f83;
    color:#fff;display:flex;align-items:center;padding:0 14px 0 20px}
  .footer-text{font-style:italic;font-size:13px;flex:1}
  .nav-btn{height:25px;padding:0 14px 0 10px;font-size:12px;color:#fff;
    background:linear-gradient(#1aa2a6,#0b7175);border:1px solid #0a5f62;
    display:flex;align-items:center;margin-left:6px;
    clip-path:polygon(0 0,88% 0,100% 50%,88% 100%,0 100%)}
  .nav-btn--back{padding:0 10px 0 14px;clip-path:polygon(12% 0,100% 0,100% 100%,12% 100%,0 50%)}

  .brand{position:absolute;left:0;width:100%;text-align:center;color:var(--navy);font-size:19px}
  .brand-dot{display:block;width:34px;height:34px;border-radius:50%;background:var(--teal);margin:0 auto 10px}
  .cover-title{position:absolute;left:0;width:100%;text-align:center;
    font-family:"PT Sans Narrow",sans-serif;font-weight:700;font-size:41px;color:var(--ink)}
  .client-name{position:absolute;left:0;width:100%;text-align:center;
    font-family:"PT Sans Narrow",sans-serif;font-weight:700;font-size:20px;color:var(--ink)}
  .client-meta{position:absolute;left:0;width:100%;text-align:center;
    font-family:"PT Sans Narrow",sans-serif;font-size:17px;color:var(--ink)}

  .flag-title{position:absolute;left:0;top:12px;display:flex;align-items:center;
    font-family:"PT Sans Narrow",sans-serif;font-weight:700;font-size:25px;color:var(--ink)}
  .flag-title svg{margin-right:6px}

  .summary{position:absolute;left:42px;width:510px;font-family:"PT Sans Narrow",sans-serif}
  .summary h3{font-size:16px;font-weight:700;color:var(--teal);margin-bottom:5px}
  .summary ul{list-style:none}
  .summary li{font-size:12.3px;line-height:18.5px;color:var(--body);position:relative;padding-left:18px}
  .summary li.point::before{content:"";position:absolute;left:0;top:3px;width:13px;height:12px;
    background:var(--teal);clip-path:polygon(0 55%,18% 40%,38% 62%,82% 0,100% 14%,40% 100%)}
  .summary li.sub{padding-left:35px}
  .summary li.sub::before{content:"";position:absolute;left:22px;top:7px;width:5px;height:5px;border-radius:50%;background:var(--teal-dark)}
  .summary li.cont{padding-left:18px}

  .corner-brand{position:absolute;right:8px;bottom:48px;color:var(--navy);font-size:15px;text-align:center}
  .corner-brand .brand-dot{width:26px;height:26px;margin-bottom:6px}
</style>
</head>
<body>

<!-- Cover, plain top -->
<section class="slide slide--tl">
  <div class="backdrop-art" role="img" aria-label="Faint leaf watermark background"></div>
  <div class="brand" style="top:46px"><span class="brand-dot"></span>Corvane Management, LLC</div>
  <h1 class="cover-title" style="top:202px">Presentation Title Here</h1>
  <div class="client-name" style="top:293px">Client Name</div>
  <div class="client-meta" style="top:320px">Client Title, Address</div>
  <footer class="footer-band"><span class="footer-text">Jakarta, 25 January 2015</span><span class="nav-btn">Enter</span></footer>
</section>

<!-- Executive summary, flag title -->
<section class="slide slide--tr">
  <div class="flag-title">
    <svg width="22" height="30" viewBox="0 0 22 30"><polygon points="0,0 22,0 14,15 22,30 0,30" fill="#2a2a2a"/></svg>
    EXECUTIVE SUMMARY
  </div>
  <div class="summary" style="top:63px">
    <h3>Corvane Management</h3>
    <ul>
      <li class="point">Harbor Financial Holdings, LLC ("HFH") is a single-purpose vehicle managed by Corvane Partners, LLC ("CVP").</li>
      <li class="point">HFH is raising $[50]-[100] MM to purchase and augment the capital base of ORL Bank ("Bank"), domiciled in Malta.</li>
      <li class="point">The Bank has a scalable, differentiated, and unconventional differentiated busines plan to:</li>
      <li class="sub">Capture attractive deposits in key EU markets, starting with Germany</li>
      <li class="sub">Purchase conservative traded Eurozone credit assets</li>
      <li class="sub">Achieve highly advantageous tax treatment to enhance equity returns</li>
      <li class="sub">Achievement of the business plan results in an ROE in excess of [25]% in Year 3</li>
      <li class="sub">Returns may be enhanced by a realization at a premium to book, as demonstrated by online comparables</li>
      <li class="point">HFH will gain control of the Bank, including 100% of voting shares and the Board of Directors</li>
      <li class="cont">If the Bank meets its business plan, a variety of highly attractive exit opportunities will be available</li>
      <li class="point">Because the company has access to bank deposits, it produces much higher returns with less risk than other companies, funds, or vehicles making leveraged investments in credit</li>
      <li class="point">It is practically impossible to form a new bank in Europe, especially for a financial sponsor;<br>this opportunity is highly scarce, and possibly unique</li>
    </ul>
  </div>
  <div class="corner-brand"><span class="brand-dot"></span>Corvane Management, LLC</div>
  <footer class="footer-band"><span class="footer-text">Corvane Management Presentation</span><span class="nav-btn nav-btn--back">Back</span><span class="nav-btn">Next</span></footer>
</section>

<!-- Cover, with header band -->
<section class="slide slide--bl">
  <div class="backdrop-art" role="img" aria-label="Faint leaf watermark background"></div>
  <header class="header-band header-band--small">Corvane Management Presentation</header>
  <div class="brand" style="top:73px"><span class="brand-dot"></span>Corvane Management, LLC</div>
  <h1 class="cover-title" style="top:208px">Presentation Title Here</h1>
  <div class="client-name" style="top:298px">Client Name</div>
  <div class="client-meta" style="top:325px">Client Title, Address</div>
  <footer class="footer-band"><span class="footer-text">Jakarta, 25 January 2015</span><span class="nav-btn">Enter</span></footer>
</section>

<!-- Executive summary, with header band -->
<section class="slide slide--br">
  <header class="header-band header-band--large">Executive Summary</header>
  <div class="summary" style="top:63px">
    <h3>Corvane Management</h3>
    <ul>
      <li class="point">Harbor Financial Holdings, LLC ("HFH") is a single-purpose vehicle managed by Corvane Partners, LLC ("CVP").</li>
      <li class="point">HFH is raising $[50]-[100] MM to purchase and augment the capital base of ORL Bank ("Bank"), domiciled in Malta.</li>
      <li class="point">The Bank has a scalable, differentiated, and unconventional differentiated busines plan to:</li>
      <li class="sub">Capture attractive deposits in key EU markets, starting with Germany</li>
      <li class="sub">Purchase conservative traded Eurozone credit assets</li>
      <li class="sub">Achieve highly advantageous tax treatment to enhance equity returns</li>
      <li class="sub">Achievement of the business plan results in an ROE in excess of [25]% in Year 3</li>
      <li class="sub">Returns may be enhanced by a realization at a premium to book, as demonstrated by online comparables</li>
      <li class="point">HFH will gain control of the Bank, including 100% of voting shares and the Board of Directors</li>
      <li class="cont">If the Bank meets its business plan, a variety of highly attractive exit opportunities will be available</li>
      <li class="point">Because the company has access to bank deposits, it produces much higher returns with less risk than other companies, funds, or vehicles making leveraged investments in credit</li>
      <li class="point">It is practically impossible to form a new bank in Europe, especially for a financial sponsor;<br>this opportunity is highly scarce, and possibly unique</li>
    </ul>
  </div>
  <div class="corner-brand"><span class="brand-dot"></span>Corvane Management, LLC</div>
  <footer class="footer-band"><span class="footer-text">Corvane Management Presentation</span><span class="nav-btn nav-btn--back">Back</span><span class="nav-btn">Next</span></footer>
</section>

</body>
</html>
```